App to show who has come in an out of a room

I need an app to show who has walked in and out of a room. I want one side to say "Chamber" and the other to say "Outside". I have attached all the pictures that I want to be able to switch left or right. I don't want the picture to disappear.
I want them to be able to switch back and forth using an Slate app.
Font styles to use
Serif
Requirements
Should not have
- The pictures of the people should not dissapear. I want to someone's finger to be able to drag them back and forth.

```html
<!DOCTYPE html>
<html lang="en">
<head>
<meta charset="utf-8">
<title>Chamber – Member Presence</title>
<link rel="stylesheet" href="https://fonts.googleapis.com/css2?family=Montserrat:wght@400;500&display=swap">
<style>
  :root{
    --bar-black:#0d0d0d;
    --nav-black:#161616;
    --text-white:#ffffff;
    --accent-cyan:#12c2e6;
    --segment-line:rgba(255,255,255,0.28);
    --row-line:rgba(255,255,255,0.18);
    --info-grey:rgba(200,200,200,0.55);
    --index-grey:#d6d6d6;
    --dome-center:#4f5a36;
    --dome-mid:#3e3a2a;
    --dome-edge:#2a1d18;
  }
  *{box-sizing:border-box;margin:0;padding:0}
  html,body{width:1200px;height:952px;overflow:hidden;background:#000}
  body{font-family:"Montserrat",sans-serif;color:var(--text-white)}
  .screen{position:relative;width:1200px;height:952px;overflow:hidden}
  .backdrop{position:absolute;left:0;top:93px;width:1200px;height:859px;
    background:radial-gradient(circle at 600px 340px,var(--dome-center) 0,#5b5a30 120px,var(--dome-mid) 330px,#3a2a22 460px,var(--dome-edge) 700px)}
  .status-bar{position:absolute;left:0;top:0;width:1200px;height:27px;background:var(--bar-black);
    font-size:13px;display:flex;align-items:center;justify-content:space-between;padding:0 8px}
  .status-left{display:flex;align-items:center;gap:6px;position:relative;z-index:1}
  .status-right{display:flex;align-items:center;gap:5px;position:relative;z-index:1}
  .status-time{position:absolute;left:0;right:0;text-align:center;font-weight:500}
  .nav-bar{position:absolute;left:0;top:27px;width:1200px;height:66px;background:var(--nav-black);
    display:flex;align-items:center;justify-content:center}
  .nav-title{font-size:25px;font-weight:400}
  .nav-menu{position:absolute;left:20px;top:19px}
  .nav-camera{position:absolute;right:16px;top:16px}
  .segment-band{position:absolute;left:0;top:93px;width:1200px;height:84px;background:rgba(90,80,70,0.45);
    border-bottom:1px solid var(--row-line)}
  .segments{position:absolute;left:19px;top:16px;width:1160px;height:49px;border:1px solid var(--segment-line);
    border-radius:25px;display:flex;overflow:hidden}
  .segment{flex:1;display:flex;align-items:center;justify-content:center;gap:12px;font-size:27px;font-weight:500}
  .segment + .segment{border-left:1px solid var(--segment-line)}
  .segment.is-active{background:var(--accent-cyan);border-radius:25px 0 0 25px}
  .member-list{position:absolute;left:0;top:177px;width:1160px;list-style:none}
  .member-row{position:relative;height:113px;border-bottom:1px solid var(--row-line);display:flex;align-items:center}
  .member-photo{position:absolute;left:19px;width:82px;height:82px;border-radius:50%}
  .member-name{position:absolute;left:133px;font-size:27px;font-weight:500}
  .member-info{position:absolute;left:1102px;width:42px;height:42px;border-radius:50%;background:var(--info-grey);
    display:flex;align-items:center;justify-content:center;font-size:24px;font-weight:500}
  .alpha-index{position:absolute;left:1168px;top:196px;width:24px;list-style:none;text-align:center;
    font-size:16px;color:var(--index-grey)}
  .alpha-index li{height:26.8px;line-height:26.8px}
  .alpha-index li.is-current{color:var(--accent-cyan)}
</style>
</head>
<body>
<main class="screen">
  <div class="backdrop" role="img" aria-label="Photograph of a stained glass chamber dome in gold, blue and violet tones"></div>

  <div class="status-bar">
    <div class="status-left"><span>Slate</span>
      <svg width="18" height="13" viewBox="0 0 18 13"><path d="M1 5a12 12 0 0 1 16 0M4 8a7.5 7.5 0 0 1 10 0M7 11a3 3 0 0 1 4 0" fill="none" stroke="#fff" stroke-width="1.8"/></svg>
    </div>
    <span class="status-time">3:14 PM</span>
    <div class="status-right"><span>32 %</span>
      <svg width="26" height="12" viewBox="0 0 26 12"><rect x="0.5" y="0.5" width="22" height="11" rx="2" fill="none" stroke="#fff"/><rect x="2" y="2" width="7" height="8" fill="#fff"/><rect x="23.5" y="4" width="2" height="4" fill="#fff"/></svg>
    </div>
  </div>

  <header class="nav-bar">
    <svg class="nav-menu" width="32" height="28" viewBox="0 0 32 28"><g stroke="#fff" stroke-width="3"><line x1="0" y1="3" x2="32" y2="3"/><line x1="0" y1="14" x2="32" y2="14"/><line x1="0" y1="25" x2="32" y2="25"/></g></svg>
    <h1 class="nav-title">Chamber</h1>
    <svg class="nav-camera" width="42" height="32" viewBox="0 0 42 32"><g fill="#fff"><path d="M4 12 L26 2 L32 12 L10 22 Z"/><rect x="28" y="14" width="4" height="10"/><rect x="28" y="22" width="12" height="4"/><rect x="20" y="16" width="8" height="3"/></g></svg>
  </header>

  <nav class="segment-band">
    <div class="segments">
      <div class="segment is-active">
        <svg width="26" height="28" viewBox="0 0 26 28"><path d="M6 2h16v24H6v-6h3v3h10V5H9v3H6z" fill="#fff"/><path d="M1 14h11M8 9l5 5-5 5" fill="none" stroke="#fff" stroke-width="3"/></svg>
        <span>Chamber</span>
      </div>
      <div class="segment">
        <svg width="30" height="24" viewBox="0 0 30 24"><g fill="#fff"><circle cx="15" cy="7" r="5"/><path d="M6 24a9 9 0 0 1 18 0z"/><circle cx="5" cy="8" r="3.5"/><circle cx="25" cy="8" r="3.5"/><path d="M0 20a6 6 0 0 1 8-5.5 11 11 0 0 0-3 5.5z"/><path d="M30 20a6 6 0 0 0-8-5.5 11 11 0 0 1 3 5.5z"/></g></svg>
        <span>All Members</span>
      </div>
      <div class="segment">
        <svg width="26" height="28" viewBox="0 0 26 28"><path d="M2 2h14v8h-3V5H5v18h8v-5h3v8H2z" fill="#fff"/><path d="M10 14h13M19 9l5 5-5 5" fill="none" stroke="#fff" stroke-width="3"/></svg>
        <span>Outside</span>
      </div>
    </div>
  </nav>

  <ul class="member-list">
    <li class="member-row"><span class="member-photo" role="img" aria-label="Portrait photo of member" style="background:#8a6a7a"></span><span class="member-name">Abernathy</span><span class="member-info">i</span></li>
    <li class="member-row"><span class="member-photo" role="img" aria-label="Portrait photo of member" style="background:#3a3436"></span><span class="member-name">Alcott</span><span class="member-info">i</span></li>
    <li class="member-row"><span class="member-photo" role="img" aria-label="Portrait photo of member" style="background:#4d6380"></span><span class="member-name">Ashford</span><span class="member-info">i</span></li>
    <li class="member-row"><span class="member-photo" role="img" aria-label="Portrait photo of member" style="background:#6b6e78"></span><span class="member-name">Brandt</span><span class="member-info">i</span></li>
    <li class="member-row"><span class="member-photo" role="img" aria-label="Portrait photo of member" style="background:#3f6e6c"></span><span class="member-name">Carrow</span><span class="member-info">i</span></li>
    <li class="member-row"><span class="member-photo" role="img" aria-label="Portrait photo of member" style="background:#2e4a58"></span><span class="member-name">Castell Reyes</span><span class="member-info">i</span></li>
    <li class="member-row"><span class="member-photo" role="img" aria-label="Portrait photo of member" style="background:#5a6a78"></span><span class="member-name">Corwin</span><span class="member-info">i</span></li>
  </ul>

  <ol class="alpha-index">
    <li class="is-current">A</li><li>B</li><li>C</li><li>D</li><li>E</li><li>F</li><li>G</li><li>H</li><li>I</li><li>J</li><li>K</li><li>L</li><li>M</li><li>N</li><li>O</li><li>P</li><li>Q</li><li>R</li><li>S</li><li>T</li><li>U</li><li>V</li><li>W</li><li>X</li><li>Y</li><li>Z</li>
  </ol>
</main>
</body>
</html>
```